Flyer-Design für Pflegedienst
Zielgruppe
Moin liebe Designer,
Wir sind ein ambulanter Intensivpflegedienst im Speckgürtel Hamburgs. Wir betreuen seit über 20 Jahren Kinder, Jugendliche und Erwachsene, die eine dauerhafte Überwachung und Betreuung benötigen. Dabei sind unsere Pflegefachkräfte dauerhaft vor Ort. Wir haben kaum Fluktuation, eine hohe Mitarbeiterzufriedenheit und erhalten auch weiterhin Bewerbungen in diesem hart umkämpften Markt.
Aufgabenstellung
Wir wollen nun in Zukunft unsere Leistungen auf einen Flyer bringen. Dazu würden wir gerne einen Flyer für die ambulante Intensivpflege erstellen lassen, die Informationen sind auf unserer Homepage unter Leistungen zu finden: https://elkor-pflegedienst.de/leistungen/ und es darf gerne ein Standart-Flyer im entsprechendem Format sein.
..und einen Flyer für unsere haushaltsnahen Dienstleistungen. Dazu haben wir die Word-Datei mit den Punkten / Leistungen erstellt und angehängt. Der Flyer soll später als Türanhänger genutzt werden können.
Für die Gestaltung kann gerne auf das bereits vorhandene Material zurück gegriffen werden.

```html
<!DOCTYPE html>
<html lang="de">
<head>
<meta charset="utf-8">
<title>Elkor Pflegedienst – Flyer</title>
<link href="https://fonts.googleapis.com/css2?family=Alegreya+Sans:wght@400;500;700;800&family=Fira+Sans:wght@400;500&display=swap" rel="stylesheet">
<style>
  :root{
    --navy:#1f3b5e;
    --sky:#5bc0eb;
    --pink:#c066a8;
    --ink:#222a33;
    --badge:#dcedf8;
    --paper:#ffffff;
  }
  *{margin:0;padding:0;box-sizing:border-box;}
  html,body{width:1200px;height:1200px;overflow:hidden;background:#fff;}
  body{font-family:"Alegreya Sans",sans-serif;color:var(--ink);}
  .flyer{position:absolute;left:175px;top:0;width:849px;height:1200px;background:var(--paper);overflow:hidden;}
  .art{position:absolute;left:0;top:0;width:849px;height:1200px;}
  .brand{position:absolute;left:40px;top:62px;color:#fff;font-family:"Alegreya Sans",sans-serif;font-weight:500;}
  .brand-name{font-size:48px;line-height:1;letter-spacing:1px;display:flex;align-items:center;gap:10px;}
  .brand-dot{width:14px;height:14px;border-radius:50%;background:#fff;display:inline-block;}
  .brand-sub{font-size:26px;margin-left:70px;margin-top:2px;}
  .badge-text{position:absolute;left:92px;top:228px;width:140px;text-align:center;font-weight:700;font-size:19px;line-height:23px;color:var(--navy);}
  .col{position:absolute;font-size:16.5px;line-height:20px;}
  .col-left{left:66px;top:424px;width:320px;}
  .col-right{left:434px;top:424px;width:340px;}
  h2{font-weight:800;font-size:19.5px;color:var(--navy);line-height:26px;}
  .list{list-style:none;}
  .list li{position:relative;padding-left:23px;}
  .list li::before{position:absolute;left:0;top:0;color:var(--sky);font-weight:700;}
  .list-x li{margin-top:8px;}
  .list-x li::before{content:"\2717";font-style:italic;}
  .list-q li{margin-top:9px;}
  .list-q li::before{content:"?";left:2px;}
  .list-check li{margin-top:8px;}
  .list-check li::before{content:"\2713";font-size:18px;}
  .para{margin-top:8px;}
  .spaced{margin-top:34px;}
  .kicker{color:var(--pink);font-weight:700;font-size:19.5px;line-height:26px;}
  .lead{color:var(--sky);font-weight:700;font-size:19.5px;line-height:23px;margin-top:4px;}
  .claim{color:var(--navy);font-weight:800;font-size:19.5px;line-height:23px;margin-top:6px;letter-spacing:.4px;}
  .intro{margin-top:30px;}
  .heart{position:absolute;left:728px;top:466px;}
  .footer{position:absolute;left:56px;top:1084px;color:#eef3f8;font-family:"Fira Sans",sans-serif;font-size:18px;line-height:24px;}
  .footer p:first-child{margin-bottom:7px;}
  .sep{color:var(--pink);margin:0 6px;}
</style>
</head>
<body>
<div class="flyer">
  <svg class="art" viewBox="0 0 849 1200" xmlns="http://www.w3.org/2000/svg">
    <defs>
      <linearGradient id="heroTone" x1="0" y1="0" x2="1" y2="0">
        <stop offset="0" stop-color="#3ba6dc"/>
        <stop offset="0.32" stop-color="#6fb3cf"/>
        <stop offset="0.5" stop-color="#c4a38f"/>
        <stop offset="0.7" stop-color="#b89a8a"/>
        <stop offset="1" stop-color="#2a3550"/>
      </linearGradient>
      <linearGradient id="cityTone" x1="0" y1="0" x2="0" y2="1">
        <stop offset="0" stop-color="#9fb6cf"/>
        <stop offset="0.55" stop-color="#a4513c"/>
        <stop offset="1" stop-color="#6d6a68"/>
      </linearGradient>
    </defs>
    <path role="img" aria-label="Foto: zwei Frauen im freundlichen Gespräch" fill="url(#heroTone)"
      d="M0 0 H849 V316 C760 340 700 372 600 366 C470 358 380 300 290 310 C180 322 80 330 0 356 Z"/>
    <circle cx="162" cy="268" r="71" fill="var(--badge)" stroke="var(--navy)" stroke-width="2"/>
    <circle cx="141" cy="206" r="22" fill="var(--pink)"/>
    <circle cx="244" cy="350" r="15" fill="var(--pink)"/>
    <circle cx="276" cy="375" r="10" fill="var(--pink)"/>
    <path fill="var(--navy)" d="M0 1081 C120 1058 200 1046 300 1046 C420 1046 520 1058 600 1056 C700 1052 780 1044 849 1041 V1200 H0 Z"/>
    <path id="ctaArc" fill="none" d="M52 1052 C160 1020 300 1010 430 1030"/>
    <text font-family="Alegreya Sans, sans-serif" font-weight="500" font-size="34" fill="var(--sky)" letter-spacing="0.5">
      <textPath href="#ctaArc">Melden Sie sich jetzt an</textPath>
    </text>
    <circle role="img" aria-label="Foto: Backsteinspeicher mit Brücke am Kanal" cx="705" cy="1069" r="105" fill="url(#cityTone)" stroke="var(--navy)" stroke-width="2"/>
    <circle cx="573" cy="969" r="15" fill="var(--pink)"/>
    <circle cx="620" cy="1004" r="20" fill="var(--pink)"/>
  </svg>

  <div class="brand">
    <div class="brand-name"><span class="brand-dot"></span>Elkor</div>
    <div class="brand-sub">Pflegedienst</div>
  </div>

  <div class="badge-text">WIR<br>SIND FÜR<br>SIE DA!</div>

  <section class="col col-left">
    <h2>Endlich einmal genug Zeit ...</h2>
    <ul class="list list-x">
      <li>für sich selbst</li>
      <li>für den Partner</li>
      <li>für Freunde</li>
      <li>für die schönen Dinge des Lebens</li>
      <li>für ...?</li>
    </ul>
    <p class="para">Jeder der Pflegt oder gepflegt wird kennt diese Situation. Luft zum Aufatmen besteht kaum noch. Die eigentlichen Freuden des Lebens werden zurückgestellt.</p>
    <h2 class="spaced">Was ist wenn:</h2>
    <ul class="list list-q">
      <li>Ich als Pflegeperson ausfalle?</li>
      <li>Ich als Pflegeperson auch noch krank werden?</li>
      <li>Ich als Pflegebedürftiger zur Belastung werde?</li>
      <li>Ich keine sozialen Kontakte aufrechterhalten kann?</li>
      <li>Ich ... ?</li>
    </ul>
  </section>

  <section class="col col-right">
    <p class="kicker">Was wäre wenn:</p>
    <p class="lead">Für Sie eine optimierte Lösung<br>gefunden wird?</p>
    <p class="claim">WIR MÖCHTEN IHNEN EIN STÜCK<br>LEBENSQUALITÄT ZURÜCKBRINGEN.</p>
    <p class="intro">Um die Leistungen aus der Pflegekasse auf Ihre Bedürfnisse zu optimieren, bieten wir weitere Leistungen an.</p>
    <ul class="list list-check">
      <li>Haushaltshilfe</li>
      <li>Einkaufshilfe</li>
      <li>Begleitung zum Friedhof</li>
      <li>Stundenweise Betreuung vor Ort</li>
      <li>Begleitung zu kulturellen Veranstaltungen/Sportveranstaltungen</li>
      <li>Betreuung und Begleitung zu Spaziergängen und Ausflügen</li>
      <li>Einfach nur zum Reden und nicht allein sein</li>
      <li>Und, und, un ...</li>
    </ul>
  </section>

  <svg class="heart" width="56" height="54" viewBox="0 0 56 54" xmlns="http://www.w3.org/2000/svg">
    <path d="M28 50 C14 38 3 28 4 16 C5 7 16 3 24 12 L28 17 L32 11 C40 2 52 6 52 16 C52 28 40 38 28 50 Z" fill="none" stroke="var(--pink)" stroke-width="1.8"/>
  </svg>

  <div class="footer">
    <p>Unser Einsatzgebiet ist Landkreis Harburg, Harburg, Winsen</p>
    <p>Elkor Pflegedienst<span class="sep">•</span>Birkenweg 12b<span class="sep">•</span>21299 Heidstedt</p>
    <p>Telefon: 040-55 0123 456<span class="sep">•</span>E-Mail: info@elkor-pflegedienst.de</p>
  </div>
</div>
</body>
</html>
```